TUMBLAVERA

We are a group of friends with a passion for ancestral knowledge of potions and medicinal formulas derived from nature. We specialise in medicinal mushrooms and adaptogens. We designed a few supplement formulas which we want to release to the market. Our team comes from biology and nutritional science background. Every product we launch will be clean in biodegradable packaging.
Our first product is a lab-tested grass-fed bovine collagen type I, II, and III mixed with organic lab-tested the most potent and bioavailable medicinal mushrooms on the market. This product will be in a pouch the print will be on the pouch or on a label, we don't know if it's possible to design a label that could be used on both? We don't know if we will be able to use organic labels yet due to the legislation changes in the UK. We are waiting for clarification.
The company is called Brindle Cove. We want to use forgotten ancestral knowledge of those potions and reintroduce them to the people. We would like our brand to look clean and friendly. A natural mix of modern and ancestral design.
Our logo and brand designs we like are attached. I have attached the source file of our logo if anyone thinks colours could be different we are open to ideas. I have also attached the visual design we were playing with on canva.com.

```html
<!DOCTYPE html>
<html lang="en">
<head>
<meta charset="utf-8">
<title>Tumblavera – Collagen Peptides &amp; Medicinal Mushrooms</title>
<link href="https://fonts.googleapis.com/css2?family=Oswald:wght@600;700&family=Poppins:wght@600&family=Roboto+Slab:wght@800&display=swap" rel="stylesheet">
<style>
  :root{
    --page:#ffffff;
    --bark:#3b2417;
    --bark-light:#5a3a27;
    --ember:#ec8a2c;
    --ember-deep:#c8562c;
    --cream:#eadbbb;
    --cream-dark:#dcc79c;
    --ink:#3a2416;
    --chalk:#f4f1ec;
  }
  *{margin:0;padding:0;box-sizing:border-box}
  html,body{width:960px;height:1200px;overflow:hidden;background:var(--page)}
  .canvas{position:relative;width:960px;height:1200px}
  .pouch{position:absolute;left:110px;top:111px;width:754px;height:972px;overflow:hidden;
    background:linear-gradient(160deg,var(--bark-light) 0%,var(--bark) 45%,var(--bark-light) 100%)}
  .brand{position:absolute;left:0;right:0;top:238px;text-align:center;
    font-family:"Poppins",sans-serif;font-weight:600;font-size:44px;color:var(--ember);letter-spacing:.5px}
  .brand-dot{display:block;width:54px;height:54px;border-radius:50%;background:var(--ember);margin:0 auto 18px}
  .product-name{position:absolute;left:0;right:0;top:350px;text-align:center;
    font-family:"Oswald",sans-serif;font-weight:700;font-size:102px;line-height:1;letter-spacing:3px;color:var(--chalk)}
  .product-name .accent{color:var(--ember)}
  .tagline{position:absolute;left:0;right:0;top:473px;text-align:center;
    font-family:"Roboto Slab",serif;font-weight:800;font-size:21px;color:var(--chalk)}
  .tagline .accent{color:var(--ember)}
  .spec{position:absolute;left:182px;width:391px;top:568px;height:60px;
    border-top:3px solid var(--chalk);border-bottom:3px solid var(--chalk);
    display:flex;align-items:center;justify-content:center;gap:16px;
    font-family:"Oswald",sans-serif;font-weight:600;font-size:26px;color:var(--chalk);letter-spacing:.5px}
  .band{position:absolute;left:0;right:0;top:708px;height:96px;background:var(--ember)}
  .bump{position:absolute;border-radius:50%;background:var(--ember)}
  .badge{position:absolute;text-align:center}
  .badge svg{display:block;margin:0 auto}
  .badge-label{font-family:"Poppins",sans-serif;font-weight:600;font-size:12px;line-height:15px;letter-spacing:1px;color:var(--cream);margin-top:6px}
  .eco-seal{position:absolute;left:526px;top:684px;width:72px;height:72px;border-radius:50%;
    background:var(--ember-deep);border:3px solid #d87a45}
  .base{position:absolute;left:0;right:0;top:804px;bottom:0;
    background:linear-gradient(180deg,var(--cream) 0%,var(--cream-dark) 100%);text-align:center;color:var(--ink);
    font-family:"Roboto Slab",serif;font-weight:800}
  .servings{position:absolute;left:0;right:0;top:38px;font-size:21px;letter-spacing:.5px}
  .net{position:absolute;left:0;right:0;top:92px;font-size:20px}
  .net strong{font-size:34px}
</style>
</head>
<body>
<div class="canvas">
  <div class="pouch">
    <div class="brand"><span class="brand-dot"></span>Brindle Cove</div>

    <h1 class="product-name">TUMB<span class="accent">LAVERA</span></h1>
    <p class="tagline"><span class="accent">Collagen Peptides</span> &amp; Medicinal Mushrooms</p>

    <div class="spec"><span>TYPE I, II, III</span><span>|</span><span>UNFLAVOURED</span></div>

    <div class="bump" style="left:136px;top:682px;width:84px;height:84px"></div>
    <div class="bump" style="left:229px;top:682px;width:84px;height:84px"></div>
    <div class="bump" style="left:419px;top:682px;width:84px;height:84px"></div>
    <div class="bump" style="left:512px;top:670px;width:100px;height:100px"></div>
    <div class="band"></div>

    <div class="badge" style="left:136px;top:700px;width:84px">
      <svg width="56" height="56" viewBox="0 0 56 56" aria-hidden="true">
        <circle cx="28" cy="28" r="25" fill="none" stroke="#f4f1ec" stroke-width="3"/>
        <rect x="18" y="18" width="20" height="20" rx="2" fill="#f4f1ec"/>
        <line x1="10" y1="46" x2="46" y2="10" stroke="#f4f1ec" stroke-width="3"/>
      </svg>
      <div class="badge-label">SUGAR<br>FREE</div>
    </div>

    <div class="badge" style="left:229px;top:700px;width:84px">
      <svg width="56" height="56" viewBox="0 0 56 56" aria-hidden="true">
        <circle cx="28" cy="28" r="25" fill="none" stroke="#f4f1ec" stroke-width="3"/>
        <line x1="28" y1="14" x2="28" y2="44" stroke="#f4f1ec" stroke-width="3"/>
        <ellipse cx="23" cy="24" rx="4" ry="6" fill="#f4f1ec"/>
        <ellipse cx="33" cy="24" rx="4" ry="6" fill="#f4f1ec"/>
        <ellipse cx="23" cy="34" rx="4" ry="6" fill="#f4f1ec"/>
        <ellipse cx="33" cy="34" rx="4" ry="6" fill="#f4f1ec"/>
        <line x1="10" y1="46" x2="46" y2="10" stroke="#f4f1ec" stroke-width="3"/>
      </svg>
    </div>

    <div class="badge" style="left:419px;top:700px;width:84px">
      <svg width="56" height="56" viewBox="0 0 56 56" aria-hidden="true">
        <circle cx="28" cy="28" r="25" fill="none" stroke="#f4f1ec" stroke-width="3"/>
        <path d="M23 14h10M25 14v10l-8 14a3 3 0 0 0 3 4h16a3 3 0 0 0 3-4l-8-14V14" fill="none" stroke="#f4f1ec" stroke-width="3" stroke-linejoin="round"/>
      </svg>
      <div class="badge-label">LAB<br>TESTED</div>
    </div>

    <div class="eco-seal" role="img" aria-label="Biodegradable and recyclable packaging seal"></div>

    <div class="base">
      <p class="servings">30 SERVINGS | FOOD SUPPLEMENT</p>
      <p class="net">NET WT <strong>360g</strong></p>
    </div>
  </div>
</div>
</body>
</html>
```